Fernvale Stationary
I need single sided standard sized Business Card [3.5" x 2"]
Prefer same font as logo, however would like to see how it looks with a different font
Simple
Suresh Kodandaraman
CEO
No. 17, 60 ft Road,
Fourth block, Hesaralu
Maranpur 570912
Sundar Pradesh
INDIA
suresh.kodand@fernvaledental.example

```html
<!DOCTYPE html>
<html lang="en">
<head>
<meta charset="utf-8">
<title>Fernvale Dental Stationery</title>
<link rel="stylesheet" href="https://fonts.googleapis.com/css2?family=Cormorant+Garamond:wght@500&family=Open+Sans:wght@400;600&display=swap">
<style>
  :root {
    --stage: #e9e6e3;
    --paper: #ffffff;
    --paper-shade: #f3f2f3;
    --plum: #5a2758;
    --plum-dark: #471d46;
    --ink: #5a5a5a;
    --faint: #ecebed;
  }
  * { margin: 0; padding: 0; box-sizing: border-box; }
  html, body { width: 1200px; height: 624px; overflow: hidden; }
  body {
    background: var(--stage);
    position: relative;
    font-family: "Open Sans", sans-serif;
    color: var(--ink);
  }
  .sheet {
    position: absolute;
    background: var(--paper);
    box-shadow: 0 2px 8px rgba(0,0,0,.18);
    overflow: hidden;
  }
  .brand {
    font-family: "Cormorant Garamond", serif;
    font-weight: 500;
    color: var(--plum);
    letter-spacing: .04em;
    white-space: nowrap;
    display: flex;
    align-items: center;
    gap: 6px;
  }
  .brand .dot {
    width: 7px; height: 7px; border-radius: 50%;
    background: currentColor; display: inline-block;
  }
  .brand-on-plum { color: var(--paper); }
  .small { font-size: 5px; line-height: 1.45; }

  /* business cards */
  .card { width: 194px; height: 100px; left: 34px; }
  .card-back-info { top: 161px; padding: 10px 12px; }
  .card-back-info .brand { font-size: 12px; }
  .card-back-info .holder { margin-top: 12px; font-size: 6px; font-weight: 600; color: var(--plum); }
  .card-back-info .role { font-size: 5px; margin-bottom: 4px; }
  .card-front-light { top: 276px; display: flex; align-items: center; justify-content: center; }
  .card-front-light .brand { font-size: 18px; }
  .card-front-plum { top: 394px; background: var(--plum); display: flex; align-items: center; justify-content: center; }
  .card-front-plum .brand { font-size: 18px; }

  /* letterheads */
  .letterhead { height: 451px; top: 101px; }
  .letterhead-main { left: 240px; width: 348px; z-index: 2; }
  .letterhead-second { left: 594px; width: 280px; z-index: 1; }
  .letterhead .brand { position: absolute; left: 22px; top: 22px; font-size: 12px; }
  .letterhead .address { position: absolute; right: 24px; top: 20px; width: 120px; }
  .letterhead .mark-faint {
    position: absolute; left: 0; right: 0; top: 190px;
    justify-content: center;
    font-size: 34px; color: var(--faint);
  }

  /* envelopes */
  .envelope-white { left: 811px; top: 182px; width: 170px; height: 118px; background: var(--paper-shade); }
  .envelope-white .brand { position: absolute; left: 30px; top: 14px; font-size: 11px; }
  .envelope-plum { left: 888px; top: 230px; width: 269px; height: 130px; z-index: 2; }
  .envelope-plum svg { position: absolute; inset: 0; }
  .envelope-plum .brand { position: absolute; left: 0; right: 0; top: 26px; justify-content: center; font-size: 13px; }

  .compliment { left: 890px; top: 384px; width: 267px; height: 130px; padding: 12px; }
  .compliment .brand { font-size: 11px; margin-bottom: 6px; }
</style>
</head>
<body>

  <section class="sheet card card-back-info">
    <div class="brand"><span class="dot"></span>Fernvale Dental</div>
    <p class="holder">Suresh Kodandaraman</p>
    <p class="role">CEO</p>
    <p class="small">No. 17, Lakeview Road,<br>Fourth block, Hesaralu<br>Maranpur 570912, Sundar Pradesh, INDIA<br>suresh.kodand@fernvaledental.example</p>
  </section>

  <section class="sheet card card-front-light">
    <div class="brand">Fernvale Dental</div>
  </section>

  <section class="sheet card card-front-plum">
    <div class="brand brand-on-plum">Fernvale Dental</div>
  </section>

  <section class="sheet letterhead letterhead-main">
    <div class="brand">Fernvale Dental</div>
    <p class="address small">No. 17, Lakeview Road,<br>Fourth block, Hesaralu<br>Maranpur 570912, Sundar Pradesh, INDIA<br><br>Phone: +91 80 4123 5678<br>Web: www.fernvaledental.example</p>
    <div class="brand mark-faint">Fernvale Dental</div>
  </section>

  <section class="sheet letterhead letterhead-second">
    <p class="address small">No. 17, Lakeview Road,<br>Fourth block, Hesaralu<br>Maranpur 570912, INDIA</p>
    <div class="brand mark-faint">Fernvale Dental</div>
  </section>

  <section class="sheet envelope-white">
    <div class="brand">Fernvale Dental</div>
  </section>

  <section class="sheet envelope-plum">
    <svg width="269" height="130" viewBox="0 0 269 130" aria-hidden="true">
      <rect width="269" height="130" fill="var(--paper-shade)"/>
      <path d="M0 0 H269 V40 L134.5 92 L0 40 Z" fill="var(--plum)"/>
      <path d="M0 40 L134.5 92 L269 40" fill="none" stroke="var(--plum-dark)" stroke-width="1"/>
    </svg>
    <div class="brand brand-on-plum">Fernvale Dental</div>
  </section>

  <section class="sheet compliment">
    <div class="brand">Fernvale Dental</div>
    <p class="small">No. 17, Lakeview Road,<br>Fourth block, Hesaralu<br>Maranpur 570912</p>
  </section>

</body>
</html>
```